Business Folder

I need a fresh, modern design for a business folder. I have our company's colors, logo, and a separate file for just the graphic part of our logo as a design element. No photo, just colors, gradients, and shadows to create depth. I like the idea of a rich grey as the background, however, I realize we'd have to lighten to 'Tax Advisory Services' part of our logo.

The design would just be the 'front' or outside of the folder from Zelvora. Design file attached. You can find that here under 9 x 12 standard folder, Left and Right Pockets With Slit Both Sides:

https://www.zelvora-example.com/content.html?id=folderDownloadTemplates&rightMenuId=rightMenu&footerId=bodyFooterStyle6

```html
<!DOCTYPE html>
<html lang="en">
<head>
<meta charset="utf-8">
<title>Corvale Tax Advisory Services – Presentation Folder</title>
<link href="https://fonts.googleapis.com/css2?family=Montserrat:wght@400;600;700&display=swap" rel="stylesheet">
<style>
  :root {
    --stage: #5b5b5b;
    --navy: #0b4f7e;
    --navy-deep: #084470;
    --azure: #2392d2;
    --sky: #62c3e6;
    --paper: #ffffff;
    --paper-shade: #e9e9ea;
    --ink: #0b4f7e;
  }
  * { box-sizing: border-box; margin: 0; padding: 0; }
  html, body { width: 1200px; height: 1200px; overflow: hidden; }
  body {
    background: var(--stage);
    font-family: "Montserrat", sans-serif;
    position: relative;
  }
  .spread {
    position: absolute;
    left: 225px;
    width: 750px;
    height: 520px;
    display: flex;
    box-shadow: 0 18px 40px rgba(0,0,0,.35);
  }
  .spread--outside { top: 50px; }
  .spread--inside { top: 625px; }
  .panel {
    position: relative;
    width: 375px;
    height: 520px;
    overflow: hidden;
    background: var(--paper);
  }
  .panel svg.art { position: absolute; inset: 0; width: 100%; height: 100%; }

  /* Wordmark */
  .wordmark {
    position: absolute;
    display: flex;
    align-items: center;
    gap: 8px;
    font-weight: 700;
    letter-spacing: 2px;
    text-transform: uppercase;
    white-space: nowrap;
  }
  .wordmark__dot { width: 14px; height: 14px; }
  .wordmark--light { color: var(--paper); }
  .wordmark--light .wordmark__dot { background: var(--paper); }
  .wordmark--dark { color: var(--navy); }
  .wordmark--dark .wordmark__dot { background: var(--azure); }

  /* Back cover */
  .panel--back { background: var(--navy); }
  .panel--back .wordmark { left: 110px; top: 360px; font-size: 28px; }
  .contact {
    position: absolute;
    left: 20px;
    right: 12px;
    top: 432px;
    display: flex;
    justify-content: space-between;
    color: var(--paper);
    font-size: 8.5px;
    line-height: 1.5;
  }
  .contact__item { display: flex; gap: 6px; align-items: flex-start; white-space: nowrap; }
  .contact__icon { width: 9px; height: 9px; margin-top: 2px; flex: none; }
  .contact__firm { font-weight: 700; }
  .contact__col { display: flex; flex-direction: column; gap: 4px; }

  /* Front cover */
  .panel--front .wordmark { left: 175px; top: 118px; font-size: 30px; }
  .headline {
    position: absolute;
    left: 100px;
    top: 285px;
    width: 265px;
    color: var(--ink);
    font-weight: 700;
    font-size: 16px;
    line-height: 1.35;
    white-space: nowrap;
  }
  .front-url {
    position: absolute;
    right: 22px;
    top: 480px;
    color: var(--paper);
    font-size: 9px;
    letter-spacing: 1px;
    white-space: nowrap;
  }

  /* Inside */
  .panel--inside-left { background: var(--paper); }
  .panel--inside-right { background: linear-gradient(90deg, var(--paper-shade), var(--paper) 40%); }
  .panel--inside-left .wordmark { left: 95px; top: 410px; font-size: 28px; }
  .business-card {
    position: absolute;
    left: 150px;
    top: 330px;
    width: 200px;
    height: 112px;
    background: var(--paper);
    box-shadow: 0 2px 5px rgba(0,0,0,.25);
  }
  .business-card .wordmark { left: 50px; top: 32px; font-size: 20px; }
  .business-card__url {
    position: absolute;
    left: 0; right: 0;
    top: 70px;
    text-align: center;
    color: var(--navy);
    font-size: 8.5px;
    font-weight: 600;
    letter-spacing: .5px;
  }
</style>
</head>
<body>

<section class="spread spread--outside" aria-label="Folder outside">
  <article class="panel panel--back" aria-label="Back cover">
    <div class="wordmark wordmark--light"><span class="wordmark__dot"></span>Corvale</div>
    <div class="contact">
      <div class="contact__col">
        <div class="contact__item">
          <svg class="contact__icon" viewBox="0 0 10 10"><path d="M5 1 L9 5 H8 V9 H2 V5 H1 Z" fill="#fff"/></svg>
          <span><span class="contact__firm">Corvale Tax Advisory Services, LLC</span><br>1420 Larkfield Road, Ste. 210<br>Brookhaven, IA 50999</span>
        </div>
        <div class="contact__item">
          <svg class="contact__icon" viewBox="0 0 10 10"><path d="M2 1 L4 1 L5 3.5 L3.8 4.5 Q5 6.5 6 6.2 L7 5 L9 6 L9 8 Q5 9.5 1 3 Z" fill="#fff"/></svg>
          <span>555-014-2290</span>
        </div>
      </div>
      <div class="contact__col">
        <div class="contact__item">
          <svg class="contact__icon" viewBox="0 0 10 10"><circle cx="5" cy="5" r="5" fill="#fff"/></svg>
          <span>800-555-0176</span>
        </div>
        <div class="contact__item">
          <svg class="contact__icon" viewBox="0 0 10 10"><circle cx="5" cy="5" r="5" fill="#fff"/></svg>
          <span>info@corvaletaxadvisory.com</span>
        </div>
        <div class="contact__item">
          <svg class="contact__icon" viewBox="0 0 10 10"><circle cx="5" cy="5" r="5" fill="#fff"/></svg>
          <span>www.CorvaleTaxAdvisory.com</span>
        </div>
      </div>
    </div>
  </article>

  <article class="panel panel--front" aria-label="Front cover">
    <svg class="art" viewBox="0 0 375 520" preserveAspectRatio="none" aria-hidden="true">
      <polygon points="0,0 150,0 0,500" fill="var(--navy)"/>
      <polygon points="205,0 375,0 375,120" fill="var(--azure)"/>
      <path d="M70,520 Q230,440 375,340 L375,520 Z" fill="var(--sky)"/>
    </svg>
    <div class="wordmark wordmark--dark"><span class="wordmark__dot"></span>Corvale</div>
    <p class="headline">We’ll review your<br>options and provide you<br>with tax-saving strategies.</p>
    <p class="front-url">www.CorvaleTaxAdvisory.com</p>
  </article>
</section>

<section class="spread spread--inside" aria-label="Folder inside">
  <article class="panel panel--inside-left" aria-label="Left pocket">
    <svg class="art" viewBox="0 0 375 520" preserveAspectRatio="none" aria-hidden="true">
      <path d="M0,330 Q170,250 330,295 Q375,310 375,360 L375,520 L0,520 Z" fill="var(--navy)"/>
    </svg>
    <div class="wordmark wordmark--light"><span class="wordmark__dot"></span>Corvale</div>
  </article>

  <article class="panel panel--inside-right" aria-label="Right pocket">
    <svg class="art" viewBox="0 0 375 520" preserveAspectRatio="none" aria-hidden="true">
      <path d="M0,520 L0,330 Q0,270 60,270 L375,270 L375,520 Z" fill="var(--navy)"/>
    </svg>
    <div class="business-card" aria-label="Business card slot">
      <div class="wordmark wordmark--dark"><span class="wordmark__dot"></span>Corvale</div>
      <p class="business-card__url">www.CorvaleTaxAdvisory.com</p>
    </div>
  </article>
</section>

</body>
</html>
```